Marketing One-Sheet for Security Deposit Claim Notice

I need a one-sheet flyer formatted for email distribution — optimized as a JPEG/PNG that I can insert into Constant Contact or Outlook. I do not want to attach it to an email, but insert it in the email we send out. I would like it to look professional but engaging. Some images would be good, but want to make sure it reads well if images do not load for the recipients. The text is in the attached Word document, but I am open to changes/ideas that may be better for marketing purposes. I included the URLs for some of the links I would like in the one-sheet that is clickable. The logo for the business is being uploaded on the Word document. Proposed text is also uploaded in a Word document. Thank you.

Target Market(s)

Landlords, Real Estate Agents, Property Managers

Industry/Entity Type

Legal

Requirements
Must have
• Professional but appealing design. The One-sheet is going to be placed in the body of emails, not as an attachment.
Nice to have
• Include our logo for the business and the web links please.
Should not have
• Images can be ok, but it needs to look right if images do not download from the email sent out.

```html
<!DOCTYPE html>
<html lang="en">
<head>
<meta charset="utf-8">
<title>Security Deposit Claim Notice – Email One-Sheets</title>
<link href="https://fonts.googleapis.com/css2?family=Cormorant+Garamond:wght@400;500&family=Montserrat:wght@400;500;600;700&display=swap" rel="stylesheet">
<style>
  :root{
    --stage-red:#9b0005;
    --brand-red:#b3121b;
    --ink:#111111;
    --text:#222222;
    --white:#ffffff;
    --band-grey:#f1f1f1;
    --serif:'Cormorant Garamond', Georgia, serif;
    --sans:'Montserrat', Arial, sans-serif;
  }
  *{box-sizing:border-box;margin:0;padding:0}
  html,body{width:1200px;height:1200px;overflow:hidden}
  body{background:radial-gradient(ellipse at center,#a80008 0%,var(--stage-red) 70%,#8a0004 100%);position:relative;font-family:var(--sans);color:var(--text)}

  .sheet{position:absolute;top:62px;width:450px;background:var(--white);box-shadow:0 6px 24px rgba(0,0,0,.35);overflow:hidden}
  .sheet--claim{left:128px;height:1076px}
  .sheet--keep{left:622px;height:1054px}
  .block{position:absolute;left:0;width:100%}

  /* header */
  .mail-header{top:0;height:89px}
  .brand{position:absolute;left:30px;top:30px}
  .brand-name{display:flex;align-items:center;gap:5px;font-family:var(--sans);font-weight:600;color:var(--ink);font-size:10px;letter-spacing:.4px;text-transform:uppercase;white-space:nowrap}
  .brand-dot{width:8px;height:8px;border-radius:50%;background:var(--brand-red);flex:none}
  .brand-web{font-size:6px;font-weight:500;color:var(--text);margin-top:5px;padding-left:13px}
  .brand-phone{font-size:6px;font-weight:700;color:var(--brand-red);padding-left:13px;margin-top:1px}
  .view-browser{position:absolute;right:30px;top:30px;width:121px;height:30px;border:1px solid #333;font-size:10px;letter-spacing:.3px;display:flex;align-items:center;justify-content:center;color:var(--ink)}

  /* hero */
  .hero{top:89px;height:115px;display:flex;align-items:center;justify-content:center;text-align:center}
  .hero--gavel{background:linear-gradient(100deg,#2b2b2b 0%,#111 35%,#1b1b1b 70%,#2a2a2a 100%)}
  .hero--keys{background:linear-gradient(180deg,#3a3a3a 0%,#1e1e1e 50%,#4a4a4a 100%)}
  .hero-title{font-family:var(--serif);font-weight:400;color:var(--white);font-size:22px;line-height:27px;letter-spacing:1px;text-transform:uppercase}

  /* photo placeholders */
  .photo{position:absolute;width:162px;height:170px;clip-path:polygon(50% 0,100% 17%,100% 100%,0 100%,0 17%)}
  .photo--keys{background:radial-gradient(circle at 45% 55%,#8a5a32 0%,#5b3a22 40%,#3b2c24 75%,#2a2420 100%)}
  .photo--book{background:linear-gradient(150deg,#5a3a2c 0%,#3e2a22 50%,#2a1a14 100%)}

  /* headings & bullets */
  .heading{font-family:var(--serif);font-weight:400;color:var(--ink);text-transform:uppercase;font-size:19px;line-height:19.5px;letter-spacing:.4px;white-space:nowrap}
  .heading .accent{color:var(--brand-red)}
  .ticks{list-style:none;margin-top:12px}
  .ticks li{position:relative;padding-left:13px;font-weight:700;font-size:10.2px;line-height:10.6px;text-transform:uppercase;color:var(--ink);margin-bottom:13px;white-space:nowrap}
  .ticks li::before{content:"";position:absolute;left:0;top:50%;width:8px;height:8px;margin-top:-4px;border-radius:50%;background:var(--brand-red)}
  .ticks li::after{content:"";position:absolute;left:2.6px;top:50%;width:2px;height:3.6px;margin-top:-2.6px;border:solid var(--white);border-width:0 1.2px 1.2px 0;transform:rotate(45deg)}
  .ticks--small li{font-size:7px;line-height:9px;margin-bottom:10px}
  .ticks--light li{font-weight:500;font-size:9.6px;line-height:13.6px;margin-bottom:8px}
  .ticks--light strong{color:var(--brand-red);font-weight:700}

  /* bands */
  .band{background:var(--band-grey);text-align:center}
  .band-title{font-family:var(--serif);font-weight:400;text-transform:uppercase;color:var(--ink);font-size:19.5px;line-height:19.5px;letter-spacing:.4px}
  .fee{color:var(--brand-red);font-weight:400;font-size:19px;letter-spacing:.3px}
  .fee b{font-weight:700}
  .band-copy{font-size:6.8px;font-weight:700;line-height:12px;text-transform:uppercase;color:var(--ink)}
  .band-para{font-size:8.6px;font-weight:400;line-height:13.6px;color:var(--text)}
  .fee-note{font-family:var(--serif);text-transform:uppercase;font-size:10px;line-height:13px;color:#333;letter-spacing:.3px}

  /* contact */
  .contact{background:linear-gradient(90deg,#151515 0%,#262626 35%,#1a1a1a 65%,#222 100%);text-align:center;color:var(--white)}
  .contact-title{font-family:var(--serif);font-weight:400;font-size:21px;letter-spacing:1px;text-transform:uppercase}
  .contact-sub{color:#d11b24;font-size:6.8px;font-weight:700;line-height:9px;text-transform:uppercase;margin-top:4px}

  /* footer */
  .mail-footer{display:flex;align-items:center;padding:0 15px}
  .footer-brand{width:120px}
  .footer-brand .brand-name{font-size:9px}
  .footer-contact{flex:1;text-align:center;font-size:7px;line-height:12px}
  .footer-contact .phone{color:var(--brand-red);font-weight:700}
  .footer-links{text-align:right;font-size:7px;line-height:12px}
</style>
</head>
<body>

<section class="sheet sheet--claim">
  <header class="block mail-header">
    <div class="brand">
      <div class="brand-name"><span class="brand-dot"></span>Landmark Lease Law</div>
      <div class="brand-web">LandmarkLeaseLaw.com</div>
      <div class="brand-phone">1(800) 555-0147</div>
    </div>
    <div class="view-browser">VIEW IN BROWSER</div>
  </header>

  <div class="block hero hero--gavel" role="img" aria-label="Dark photo of a gavel and eyeglasses on a desk">
    <h1 class="hero-title">Security Deposit<br>Claim Notice</h1>
  </div>

  <div class="block" style="top:204px;height:230px">
    <div style="position:absolute;left:30px;top:58px;width:220px">
      <h2 class="heading">Keep the Tenant’s<br><span class="accent">Security Deposit</span></h2>
      <ul class="ticks">
        <li>Cover unpaid rent</li>
        <li>Apply to legal fees and costs</li>
        <li>Charge against damages<br>to the property</li>
      </ul>
    </div>
    <div class="photo photo--keys" style="left:258px;top:30px" role="img" aria-label="House-shaped key ring on a wooden sound block beside a gavel"></div>
  </div>

  <div class="block band" style="top:434px;height:112px;padding-top:20px">
    <h2 class="band-title">We Prepare Security Deposit<br>Claim Notices</h2>
    <p class="fee" style="margin-top:10px">FLAT FEE <b>$350</b></p>
  </div>

  <div class="block" style="top:546px;height:223px">
    <div class="photo photo--book" style="left:30px;top:25px" role="img" aria-label="Gavel resting on a landlord-tenant law book"></div>
    <div style="position:absolute;left:225px;top:52px;width:215px">
      <h2 class="heading" style="font-size:18px">Follow Florida Law<br>to Keep the Deposit</h2>
      <ul class="ticks ticks--small" style="margin-top:12px">
        <li>Tenant is automatically<br>entitled to their full deposit back</li>
        <li>No claim against the deposit can be made</li>
        <li>Tenant can sue and recover the deposit<br>and thousands in legal fees</li>
      </ul>
    </div>
  </div>

  <div class="block band" style="top:769px;height:143px;padding-top:23px">
    <p class="band-copy">There are lawyers that specialize in representing tenants and go after<br>landlords that do not make a proper claim against the security deposit.<br>They sue and win their cases and get thousands of dollars in legal<br>fees against landlords, even if the tenant owes unpaid rent.</p>
    <p class="fee-note" style="font-size:14px;margin-top:10px">For commercial properties,</p>
    <p class="fee" style="font-size:19.5px;line-height:20px">THE FLAT LEGAL FEE IS <b>$450</b></p>
  </div>

  <div class="block contact" style="top:912px;height:98px;padding-top:26px" role="img" aria-label="Dark photo of professionals meeting at a table">
    <h2 class="contact-title">Contact Us</h2>
    <p class="contact-sub">Hire us to prepare and serve to the tenant<br>the security deposit claim</p>
  </div>

  <footer class="block mail-footer" style="top:1010px;height:66px">
    <div class="footer-brand"><div class="brand-name"><span class="brand-dot"></span>Landmark Lease Law</div></div>
    <div class="footer-contact">www.LandmarkLeaseLaw.com<br><span class="phone">1800-555-0147</span></div>
    <div class="footer-links">More Information<br>Request Our Hiring Documents</div>
  </footer>
</section>

<section class="sheet sheet--keep">
  <header class="block mail-header">
    <div class="brand">
      <div class="brand-name"><span class="brand-dot"></span>Landmark Lease Law</div>
      <div class="brand-web">LandmarkLeaseLaw.com</div>
      <div class="brand-phone">1(800) 555-0147</div>
    </div>
    <div class="view-browser">VIEW IN BROWSER</div>
  </header>

  <div class="block hero hero--keys" role="img" aria-label="Dark photo of a hand passing keys over a small house model">
    <h1 class="hero-title">Landlord, Need to Keep the<br>Security Deposit?</h1>
  </div>

  <div class="block" style="top:204px;height:230px">
    <div style="position:absolute;left:30px;top:48px;width:220px">
      <h2 class="heading">Security Deposit<br>Claim Notice<br>Requirements:</h2>
      <ul class="ticks" style="margin-top:14px">
        <li>Must be served on time</li>
        <li>Must be served according<br>to Florida law</li>
        <li>Must contain specific wording</li>
      </ul>
    </div>
    <div class="photo photo--keys" style="left:258px;top:30px" role="img" aria-label="House-shaped key ring on a wooden sound block beside a gavel"></div>
  </div>

  <div class="block" style="top:434px;height:199px">
    <div class="photo photo--book" style="left:30px;top:0" role="img" aria-label="Gavel resting on a landlord-tenant law book"></div>
    <div style="position:absolute;left:221px;top:20px;width:215px">
      <h2 class="heading">Security Deposit<br>Claim Notice Not<br>Correct, Then:</h2>
      <ul class="ticks ticks--light" style="margin-top:10px">
        <li>Tenant could demand return<br>of <strong>full security deposit</strong></li>
        <li>Tenant can sue and recover<br><strong>legal fees from the landlord</strong></li>
      </ul>
    </div>
  </div>

  <div class="block band" style="top:633px;height:261px;padding:29px 38px 0">
    <p class="band-para">There are lawyers that specialize in representing <b>TENANTS</b> against landlords for not making a proper claim on the security deposit. They can win the case and recover thousands of dollars $$ in legal fees from the Landlord. Plus, the tenant can get back 100% of the Security Deposit, even if they owe the Landlord unpaid rent or caused damages to the property. Florida law helps the tenants if the Security Deposit Claim Notice is not served on time and correctly.</p>
    <p class="fee" style="margin-top:20px"><b>$350</b> FLAT FEE</p>
    <p class="fee-note">To prepare and serve security deposit<br>claim notices for landlords.</p>
    <p class="fee" style="margin-top:12px"><b>$450</b> FLAT FEE</p>
    <p class="fee-note">For commercial properties</p>
  </div>

  <div class="block contact" style="top:894px;height:99px;padding-top:26px" role="img" aria-label="Dark photo of professionals meeting at a table">
    <h2 class="contact-title">Contact Us</h2>
    <p class="contact-sub">Contact us to prepare the security<br>deposit claim notice.</p>
  </div>

  <footer class="block mail-footer" style="top:993px;height:61px">
    <div class="footer-brand"><div class="brand-name"><span class="brand-dot"></span>Landmark Lease Law</div></div>
    <div class="footer-contact">www.LandmarkLeaseLaw.com<br><span class="phone">1800-555-0147</span></div>
    <div class="footer-links">More Information<br>Request Our Hiring Documents</div>
  </footer>
</section>

</body>
</html>
```